I need a business card for my Heating / Cooling Business. I've been in the business for 28 years. The name of the company is "Walt's Heating and Cooling".
Designers, I've attached an old business card we've used to copy the information.
Take off 15 years of experience
Business
Walt Pemberton and Marla Pemberton(740)-795-4758

```html
<!DOCTYPE html>
<html lang="en">
<head>
<meta charset="utf-8">
<title>Walt's Heating &amp; Cooling – Business Card</title>
<link rel="stylesheet" href="https://fonts.googleapis.com/css2?family=Open+Sans:wght@400;600;700&display=swap">
<style>
  :root {
    --page-bg: #e9e7e3;
    --card-white: #f7f6f2;
    --teal-deep: #35b1b4;
    --teal-light: #86d2c9;
    --ink: #6b6b6b;
    --ink-strong: #5e5e5e;
    --logo-white: #ffffff;
  }
  * { margin: 0; padding: 0; box-sizing: border-box; }
  html, body {
    width: 1200px; height: 800px; overflow: hidden;
    background: var(--page-bg);
    font-family: "Open Sans", sans-serif;
  }
  .card {
    position: absolute; left: 150px; top: 143px;
    width: 900px; height: 514px;
    background: var(--card-white);
    box-shadow: 0 10px 30px rgba(0,0,0,0.18);
    overflow: hidden;
  }
  .card__panel { position: absolute; inset: 0; }
  .brand {
    position: absolute; left: 40px; top: 170px; width: 300px;
    text-align: center; color: var(--logo-white); font-weight: 600;
  }
  .brand__mark {
    width: 120px; height: 120px; border-radius: 50%;
    background: var(--logo-white); margin: 0 auto 22px;
  }
  .brand__name { font-size: 38px; line-height: 1.1; letter-spacing: 1px; }
  .brand__tagline { font-size: 21px; line-height: 1.3; letter-spacing: 0.5px; }
  .details {
    position: absolute; left: 470px; top: 70px; width: 380px;
    text-align: center; color: var(--ink); text-transform: uppercase;
  }
  .details__heading {
    font-size: 22px; font-weight: 700; color: var(--ink-strong);
    letter-spacing: 0.3px; margin-bottom: 14px;
  }
  .services { list-style: none; font-size: 16px; line-height: 1.35; }
  .contact {
    margin-top: 52px; font-size: 16px; line-height: 1.4;
    display: flex; justify-content: center; align-items: flex-start; gap: 12px;
  }
  .contact__icon { width: 18px; height: 18px; margin-top: 12px; flex: none; }
  .address { margin-top: 62px; font-size: 16px; line-height: 1.4; }
</style>
</head>
<body>
  <section class="card">
    <svg class="card__panel" width="900" height="514" viewBox="0 0 900 514" role="img" aria-label="Teal panel with soft geometric pattern">
      <defs>
        <linearGradient id="tealPanel" x1="0" y1="0" x2="1" y2="1">
          <stop offset="0" stop-color="var(--teal-deep)"/>
          <stop offset="1" stop-color="var(--teal-light)"/>
        </linearGradient>
      </defs>
      <polygon points="0,0 430,0 370,270 540,514 0,514" fill="url(#tealPanel)"/>
    </svg>

    <div class="brand">
      <div class="brand__mark"></div>
      <div class="brand__name">WALT'S</div>
      <div class="brand__tagline">HEATING &amp; COOLING</div>
    </div>

    <div class="details">
      <h2 class="details__heading">Installation &amp; Service</h2>
      <ul class="services">
        <li>Small Appliance Repair</li>
        <li>Plumbing</li>
        <li>Refrigiration</li>
        <li>Car Airconditioning</li>
        <li>Professional Mobile Home Installation</li>
      </ul>
      <div class="contact">
        <svg class="contact__icon" viewBox="0 0 24 24" aria-hidden="true">
          <path fill="var(--ink)" d="M6.6 10.8a15.1 15.1 0 0 0 6.6 6.6l2.2-2.2a1 1 0 0 1 1-.25 11.4 11.4 0 0 0 3.6.57 1 1 0 0 1 1 1V20a1 1 0 0 1-1 1A17 17 0 0 1 3 4a1 1 0 0 1 1-1h3.5a1 1 0 0 1 1 1c0 1.25.2 2.45.57 3.6a1 1 0 0 1-.25 1z"/>
        </svg>
        <div>
          <div>Walt Pemberton &amp; Marla Pemberton</div>
          <div>(555)-312-9064</div>
        </div>
      </div>
      <div class="address">
        <div>41820 Maple Drive</div>
        <div>Fairview Point, Ohio 43000</div>
      </div>
    </div>
  </section>
</body>
</html>
```